Japanese Rice Food Package Label

- We are launching Japanese food products to the outdoor community.
- Made in Japan
- We will have multiple flavors of rice but want to keep the package label almost the same and only replace the flavor text (e.g., Mixed Rice, Curry Rice, etc)
- We like simple designs inspired by Japan.
- Label size: 105 mm x148 mm
- Our brand: YOBEN https://yoben.co/
- Video message: https://www.vidqo.com/share/3f51b07a9e2c4d6891a0c7e5b2d94f18

```html
<!DOCTYPE html>
<html lang="en">
<head>
<meta charset="utf-8">
<title>YOBEN – Mixed Rice Label</title>
<link rel="stylesheet" href="https://fonts.googleapis.com/css2?family=Montserrat:wght@300;400;800&family=Zen+Kurenaido&display=swap">
<style>
  :root {
    --page: #f4f4f2;
    --label: #e2dbb5;
    --wave-light: #d3cba7;
    --wave-dark: #c6bd97;
    --dots: rgba(160, 150, 120, 0.22);
    --sun: #e03a3a;
    --flavor-red: #9e3f47;
    --ink: #1c1c1c;
    --frame-red: #e03a3a;
  }
  * { margin: 0; padding: 0; box-sizing: border-box; }
  html, body {
    width: 1200px; height: 900px; overflow: hidden;
    background: var(--page);
  }
  .label {
    position: absolute; left: 33px; top: 48px;
    width: 840px; height: 595px;
    transform: scale(1.35); transform-origin: 0 0;
    background: var(--label);
    overflow: hidden;
    font-family: "Montserrat", sans-serif;
    color: var(--ink);
  }
  .wave-panel {
    position: absolute; left: 0; top: 0;
    width: 213px; height: 510px;
    background: linear-gradient(180deg, var(--wave-light), var(--wave-dark));
  }
  .flavor-vertical {
    position: absolute; left: 48px; top: 36px; width: 62px;
    display: flex; flex-direction: column; align-items: center;
    font-family: "Zen Kurenaido", sans-serif;
    font-size: 40px; line-height: 51px;
    color: var(--flavor-red);
  }
  .sun {
    position: absolute; left: 128px; top: 63px;
    width: 320px; height: 320px; border-radius: 50%;
    background: var(--sun);
  }
  .rice-bowl-art {
    position: absolute; left: 263px; top: 150px;
    width: 327px; height: 290px;
    background: radial-gradient(ellipse at 50% 45%, rgba(40, 35, 30, 0.16), rgba(40, 35, 30, 0) 70%);
  }
  .dot-field { position: absolute; background: var(--dots); border-radius: 6px; }
  .dot-field--top { left: 544px; top: 16px; width: 198px; height: 202px; }
  .dot-field--bottom { left: 199px; top: 516px; width: 148px; height: 68px; }
  .brand-box {
    position: absolute; left: 694px; top: 45px;
    width: 108px; height: 345px;
    border: 1.5px solid var(--ink);
    display: flex; align-items: center; justify-content: center;
  }
  .brand-name {
    transform: rotate(-90deg);
    font-weight: 800; font-size: 80px; letter-spacing: 1px;
    white-space: nowrap; line-height: 1;
  }
  .flavor-box {
    position: absolute; left: 313px; top: 455px;
    width: 400px; height: 73px;
    border: 1.5px solid var(--frame-red);
    display: flex; align-items: center; justify-content: center;
  }
  .flavor-name {
    font-weight: 300; font-size: 44px; letter-spacing: 2px;
  }
  .origin {
    position: absolute; left: 313px; top: 541px; width: 400px;
    text-align: center;
    font-size: 10.5px; font-weight: 400; letter-spacing: 3.5px;
  }
</style>
</head>
<body>
  <main class="label">
    <div class="wave-panel" role="img" aria-label="Traditional Japanese wave pattern in soft tan"></div>
    <div class="flavor-vertical" aria-label="Mixed Rice">
      <span>M</span><span>I</span><span>X</span><span>E</span><span>D</span><span>R</span><span>I</span><span>C</span><span>E</span>
    </div>
    <div class="dot-field dot-field--top" role="img" aria-label="Grid of small tan dots"></div>
    <div class="dot-field dot-field--bottom" role="img" aria-label="Grid of small tan dots"></div>
    <div class="sun"></div>
    <div class="rice-bowl-art" role="img" aria-label="Line drawing of a bowl of mixed rice with chopsticks"></div>
    <div class="brand-box"><span class="brand-name">YOBEN</span></div>
    <div class="flavor-box"><h1 class="flavor-name">MIXED RICE</h1></div>
    <p class="origin">MADE IN JAPAN</p>
  </main>
</body>
</html>
```